VaultMeridan Business Card Re-Design

VaultMeridan is a specialized information security company that applies its proven methodology of security Assessment, Development, Integration and Training (A-D-I-T) to provide cyber security services in the areas of Data Protection, Network Defense and Compliance. We need the current business card re-designed to properly scale the fonts and possibly rearranging some elements (icons, lettering, etc.) to make the card more appealing to the eye. The card should have the logo that is on the web site (www.vaultmeridan-example.com). We would like ideas for both a black card (black background) and a white card (white background). We prefer rounded corners to help the card stand out but are open to all ideas. FYI: VaultMeridan's slogan is "...your security is our business".

Target Market(s)

#1 US Government Contracting Companies, #2 Commercial Companies, #3 Gen. Public.

Industry/Entity Type

Business

Contact Information for Business Card

See Description; open to the use of different fonts.

Font styles to use
Sans Serif

Colors
000000
ec1f27
ffffff

Requirements
Must have
• Company logo on web site, rounded corners, list of company offerings on the back of the card.
Nice to have
• Icons
Should not have
• none

```html
<!DOCTYPE html>
<html lang="en">
<head>
<meta charset="utf-8">
<title>VaultMeridan Business Card</title>
<link href="https://fonts.googleapis.com/css2?family=Roboto+Condensed:wght@700&family=Saira+Condensed:wght@400;500&family=Saira+Semi+Condensed:wght@400&display=swap" rel="stylesheet">
<style>
  :root {
    --black: #000000;
    --card-black: #111111;
    --band-grey: #262626;
    --column-grey: #1c1c1c;
    --red: #ec1f27;
    --white: #ffffff;
    --muted: #bdbdbd;
    --backdrop: #e9e7e3;
  }
  * { margin: 0; padding: 0; box-sizing: border-box; }
  html, body { width: 1200px; height: 880px; overflow: hidden; }
  body {
    background: var(--backdrop);
    font-family: "Saira Condensed", sans-serif;
    position: relative;
  }
  .card {
    position: absolute;
    top: 280px;
    width: 570px;
    height: 320px;
    background: var(--card-black);
    overflow: hidden;
    color: var(--white);
    box-shadow: 0 6px 18px rgba(0,0,0,0.18);
  }
  .card--front { left: 20px; }
  .card--back { left: 610px; }

  /* Front */
  .brand-band {
    position: absolute; left: 0; top: 0; width: 100%; height: 82px;
    background: var(--band-grey);
  }
  .brand-name {
    position: absolute; left: 34px; top: 12px;
    font-weight: 500; font-size: 32px; letter-spacing: 4px; color: var(--white);
  }
  .brand-tagline {
    position: absolute; left: 36px; top: 56px;
    font-family: "Saira Condensed", sans-serif;
    font-size: 13px; letter-spacing: 2.5px; color: var(--muted);
  }
  .identity {
    position: absolute; left: 26px; top: 125px;
    border-left: 5px solid var(--red);
    padding-left: 12px;
  }
  .identity__name {
    font-family: "Roboto Condensed", sans-serif; font-weight: 700;
    font-size: 35px; line-height: 36px; color: var(--white);
  }
  .identity__title { font-size: 23px; line-height: 26px; color: var(--red); }
  .identity__creds { font-size: 15px; line-height: 18px; color: var(--red); }

  .icon-column {
    position: absolute; left: 298px; top: 82px; width: 60px; height: 210px;
    background: var(--column-grey);
    border-left: 4px solid var(--red);
    border-right: 4px solid var(--red);
  }
  .icon { position: absolute; left: 8px; width: 36px; height: 32px; }
  .contact-list {
    position: absolute; left: 372px; top: 82px; width: 190px; list-style: none;
    font-size: 19px; line-height: 22px; color: var(--white);
  }
  .contact-list li { position: absolute; left: 0; white-space: nowrap; }
  .contact-list .small { font-size: 14px; line-height: 18px; }

  .address-band {
    position: absolute; left: 0; bottom: 0; width: 100%; height: 28px;
    background: var(--red);
    font-size: 14px; line-height: 28px; text-align: center; color: var(--white);
    white-space: nowrap;
  }
  .address-band .sep { color: var(--black); }

  /* Back */
  .top-rule {
    position: absolute; left: 0; top: 4px; width: 100%; height: 4px; background: var(--red);
  }
  .back-brand {
    position: absolute; left: 0; top: 26px; width: 100%; text-align: center;
    font-weight: 500; font-size: 28px; letter-spacing: 4px; color: var(--white);
  }
  .offerings {
    position: absolute; top: 88px; list-style: none;
    font-size: 15px; line-height: 26px; color: var(--white);
  }
  .offerings--left { left: 40px; }
  .offerings--right { left: 345px; }
  .offerings--center { left: 0; width: 100%; text-align: center; top: 246px; }
  .offerings li { white-space: nowrap; }
  .offerings li::before {
    content: ""; display: inline-block; width: 10px; height: 10px;
    background: var(--red); margin-right: 14px; vertical-align: 1px;
  }
  .slogan-band {
    position: absolute; left: 0; bottom: 0; width: 100%; height: 38px;
    background: var(--band-grey); text-align: center;
  }
  .slogan { font-size: 16px; letter-spacing: 1.5px; line-height: 22px; padding-top: 4px; color: var(--red); }
  .back-url { font-size: 9px; color: var(--white); line-height: 10px; letter-spacing: 0.5px; }
</style>
</head>
<body>

<section class="card card--front" aria-label="Business card front">
  <div class="brand-band">
    <div class="brand-name">VaultMeridan</div>
    <div class="brand-tagline">INFORMATION SECURITY</div>
  </div>

  <div class="identity">
    <div class="identity__name">Marcus Hale</div>
    <div class="identity__title">President-CEO</div>
    <div class="identity__creds">CISSP,C|EH</div>
  </div>

  <div class="icon-column">
    <svg class="icon" style="top:18px" viewBox="0 0 36 32" aria-label="Phone">
      <polygon points="9,1 27,1 35,16 27,31 9,31 1,16" fill="#ec1f27"/>
      <path d="M12 9c1-1 2-1 3 0l1.5 2c.5.8.3 1.5-.3 2l-1 .8c.8 1.8 2.2 3.2 4 4l.8-1c.5-.6 1.2-.8 2-.3l2 1.5c1 1 1 2 0 3l-1 1c-4 1-11-6-10-10z" fill="#fff"/>
    </svg>
    <svg class="icon" style="top:63px" viewBox="0 0 36 32" aria-label="Mobile">
      <polygon points="9,1 27,1 35,16 27,31 9,31 1,16" fill="#ec1f27"/>
      <rect x="13" y="7" width="10" height="18" rx="1.5" fill="none" stroke="#fff" stroke-width="2"/>
      <circle cx="18" cy="22" r="1" fill="#fff"/>
    </svg>
    <svg class="icon" style="top:110px" viewBox="0 0 36 32" aria-label="Website">
      <polygon points="9,1 27,1 35,16 27,31 9,31 1,16" fill="#ec1f27"/>
      <g fill="none" stroke="#fff" stroke-width="1.6">
        <circle cx="18" cy="16" r="8"/>
        <ellipse cx="18" cy="16" rx="3.5" ry="8"/>
        <line x1="10" y1="16" x2="26" y2="16"/>
        <line x1="11.5" y1="12" x2="24.5" y2="12"/>
        <line x1="11.5" y1="20" x2="24.5" y2="20"/>
      </g>
    </svg>
    <svg class="icon" style="top:158px" viewBox="0 0 36 32" aria-label="Email">
      <polygon points="9,1 27,1 35,16 27,31 9,31 1,16" fill="#ec1f27"/>
      <rect x="10" y="10" width="16" height="12" fill="none" stroke="#fff" stroke-width="1.8"/>
      <polyline points="10,10 18,17 26,10" fill="none" stroke="#fff" stroke-width="1.8"/>
    </svg>
  </div>

  <ul class="contact-list">
    <li style="top:20px">555.014.2201</li>
    <li style="top:65px">555.018.3627</li>
    <li style="top:117px" class="small">www.vaultmeridan-example.com</li>
    <li style="top:152px" class="small">info@vaultmeridan-example.com</li>
    <li style="top:172px" class="small">mhale@vaultmeridan-example.com</li>
  </ul>

  <div class="address-band">VaultMeridan, Inc. <span class="sep">//</span> 1200 Harbor Ridge Rd. Suite 300 <span class="sep">//</span> Springdale, Maryland 20999</div>
</section>

<section class="card card--back" aria-label="Business card back">
  <div class="top-rule"></div>
  <div class="back-brand">VaultMeridan</div>

  <ul class="offerings offerings--left">
    <li>Network Attack Penetration and Defense</li>
    <li>Foreign/Counter Intelligence Data Security</li>
    <li>Security Subject Matter Experts</li>
    <li>Secure Cloud and Open Stack Solutions</li>
    <li>Executive Security Strategy Coaching</li>
    <li>Classified Cross Domain Solutions</li>
  </ul>
  <ul class="offerings offerings--right">
    <li>Red/Blue Team</li>
    <li>Data Center Consolidation</li>
    <li>Secure Wireless Solutions</li>
    <li>Secure Virtual Computing</li>
    <li>Data Encryption/Privacy</li>
    <li>Certification and Accredition</li>
  </ul>
  <ul class="offerings offerings--center">
    <li>Security Training, Assessment and Integration</li>
  </ul>

  <div class="slogan-band">
    <div class="slogan">"your security is our business"</div>
    <div class="back-url">www.vaultmeridan-example.com</div>
  </div>
</section>

</body>
</html>
```